Defend science flier

Put my name and text below on one side of flier, and place other text on other side. Try to keep file about 4 by 6 or 6 by 8 inches.

Target Market(s)

Community and retailers.

Industry/Entity Type

Retail and concerned community.

Font styles to use
Serif

Requirements
Must have
• Good, eye-catching titles. Be smaller format. Not 8 by 11
Nice to have
• Black and white text. Maybe bullets etc for organizion but no decorations.
Should not have
• Any decoration

```html
<!DOCTYPE html>
<html lang="en">
<head>
<meta charset="utf-8">
<title>Defend Science Flyer – Martin R. Halvorsen</title>
<link href="https://fonts.googleapis.com/css2?family=Tinos&family=Source+Sans+3:ital,wght@0,400;0,600;1,400&display=swap" rel="stylesheet">
<style>
  :root {
    --board: #6d6e71;
    --gold: #b39a5a;
    --gold-light: #d8c48e;
    --gold-dark: #8e7a47;
    --stone: #7d735f;
    --paper: #fdfdf8;
    --ink: #1a1a1a;
    --white: #ffffff;
  }
  * { box-sizing: border-box; margin: 0; padding: 0; }
  html, body { width: 1200px; height: 494px; overflow: hidden; }
  body { background: var(--board); position: relative; font-family: "Source Sans 3", Arial, sans-serif; color: var(--ink); }

  .size-note { position: absolute; left: 71px; top: 42px; font-size: 9px; color: var(--white); }

  .flyer {
    position: absolute; top: 75px; width: 519px; height: 343px;
    box-shadow: 0 2px 6px rgba(0,0,0,.35);
  }
  .flyer--front { left: 62px; }
  .flyer--back { left: 629px; }

  .flyer__backdrop {
    position: absolute; inset: 0;
    background: linear-gradient(180deg, var(--stone) 0%, var(--gold-dark) 10%, var(--gold) 22%, var(--gold) 75%, var(--gold-light) 100%);
  }
  .flyer__backdrop::before, .flyer__backdrop::after {
    content: ""; position: absolute; top: 0; bottom: 0; width: 40px;
    background: linear-gradient(90deg, rgba(120,110,90,.55), rgba(200,185,140,.35));
  }
  .flyer__backdrop::before { left: 0; }
  .flyer__backdrop::after { right: 0; }

  .panel {
    position: absolute; left: 24px; top: 19px; width: 475px; height: 311px;
    background: var(--paper); border-radius: 5px;
  }

  .panel__title {
    position: absolute; left: 0; right: 0; top: 25px; text-align: center;
    font-family: "Tinos", "Times New Roman", serif; font-weight: 400; font-size: 27px; line-height: 1.2;
  }

  .col { position: absolute; top: 81px; font-size: 10.2px; line-height: 1.2; }
  .col--left { left: 18px; width: 200px; }
  .col--right { left: 255px; width: 200px; text-align: justify; }
  .col--right p { margin-bottom: 12px; }
  .divider { position: absolute; left: 236px; top: 79px; height: 160px; width: 1px; background: var(--gold); }

  .sins { list-style: none; margin-top: 4px; }
  .sins li { display: flex; align-items: center; gap: 5px; height: 28.5px; }
  .sins__num {
    flex: none; width: 19px; height: 19px; border-radius: 50%;
    border: 1px solid var(--gold); box-shadow: inset 0 0 0 2px var(--paper), inset 0 0 0 3px var(--gold-light);
    display: flex; align-items: center; justify-content: center;
    font-family: "Tinos", "Times New Roman", serif; font-size: 11px;
  }

  .cta { position: absolute; left: 0; right: 0; top: 262px; text-align: center; }
  .cta__label { font-family: "Tinos", "Times New Roman", serif; font-size: 12px; line-height: 14px; letter-spacing: .2px; }
  .cta__url {
    display: inline-block; margin-top: 6px; width: 248px; height: 21px; line-height: 21px;
    border-radius: 11px; background: var(--gold); color: var(--white); font-size: 13px;
  }

  .profile__name {
    position: absolute; left: 0; right: 0; top: 23px; text-align: center;
    font-family: "Tinos", "Times New Roman", serif; font-weight: 400; font-size: 29px; line-height: 1.2;
  }
  .profile__tagline {
    position: absolute; left: 0; right: 0; top: 60px; text-align: center;
    font-family: "Tinos", "Times New Roman", serif; font-size: 10.5px;
  }
  .profile__rule { position: absolute; left: 108px; top: 81px; }

  .claims { position: absolute; left: 30px; width: 416px; top: 100px; list-style: none; font-size: 10.5px; line-height: 1.25; }
  .claims li { position: relative; padding-left: 12px; margin-bottom: 11px; }
  .claims svg { position: absolute; left: 0; top: 2px; }
  .claims blockquote { font-style: italic; margin-top: 12px; text-align: justify; }
</style>
</head>
<body>
  <div class="size-note">Flyer size: 4x6</div>

  <section class="flyer flyer--front">
    <div class="flyer__backdrop" role="img" aria-label="Classical stone columns framing a gold background"></div>
    <div class="panel">
      <h1 class="panel__title">Why Did the Culture Change?</h1>

      <div class="col col--left">
        <p>During the 1960s, we socialized the Seven Deadly Sins. Therefore:</p>
        <ol class="sins">
          <li><span class="sins__num">1</span><span>Pride became “Racism.”</span></li>
          <li><span class="sins__num">2</span><span>Lust became “Sexism” and “Gender” existing “out there.”</span></li>
          <li><span class="sins__num">3</span><span>Gluttony became “Consumer Fetishism.”</span></li>
          <li><span class="sins__num">4</span><span>Vanity became “Media Images of Beauty.”</span></li>
          <li><span class="sins__num">5</span><span>Sloth became The lack of social action: “Are you fighting for diversity?”</span></li>
        </ol>
      </div>

      <div class="divider"></div>

      <div class="col col--right">
        <p>This “fight for diversity” inspires attacks against people like Dr. Halvorsen for asserting any reality principle about human nature.</p>
        <p>These thugs are religious crusaders who ignore the rule of law and try to stop the progress of science. These fanatics go around and give people a “tear-test”-as during the Salem witch trials. Don’t let them take over.</p>
        <p>The educational and culture elites-such as Hollywood-now reject these theological “social sins.” The elites are replacing theology with traditional, human-based sin.</p>
      </div>

      <div class="cta">
        <div class="cta__label">SEE MARTIN’S HOMEPAGE FOR MORE DETAILS:</div>
        <div class="cta__url">www.martin-halvorsen.org</div>
      </div>
    </div>
  </section>

  <section class="flyer flyer--back">
    <div class="flyer__backdrop" role="img" aria-label="Classical stone columns framing a gold background"></div>
    <div class="panel">
      <h2 class="profile__name">Martin R. Halvorsen, Ph.D</h2>
      <p class="profile__tagline">“The Cornerstone of Psychology and History.”</p>
      <svg class="profile__rule" width="260" height="4" viewBox="0 0 260 4" aria-hidden="true">
        <path d="M0 2 Q130 -0.5 260 2 Q130 4.5 0 2Z" fill="#b39a5a"/>
      </svg>

      <ul class="claims">
        <li><svg width="9" height="9" viewBox="0 0 9 9" aria-hidden="true"><circle cx="4.5" cy="4.5" r="4" fill="none" stroke="#b39a5a"/><path d="M3.5 2.7 5.3 4.5 3.5 6.3" fill="none" stroke="#b39a5a"/></svg>Martin’s Bio-Psych has Restructured the Liberal Arts and Sciences—from Genetics to the Fine Arts and Hollywood.</li>
        <li><svg width="9" height="9" viewBox="0 0 9 9" aria-hidden="true"><circle cx="4.5" cy="4.5" r="4" fill="none" stroke="#b39a5a"/><path d="M3.5 2.7 5.3 4.5 3.5 6.3" fill="none" stroke="#b39a5a"/></svg>Museum Catalogues, Better Nonfiction, and Hollywood Films Now Use Martin’s Methods.</li>
        <li><svg width="9" height="9" viewBox="0 0 9 9" aria-hidden="true"><circle cx="4.5" cy="4.5" r="4" fill="none" stroke="#b39a5a"/><path d="M3.5 2.7 5.3 4.5 3.5 6.3" fill="none" stroke="#b39a5a"/></svg>Martin’s Biopsych is endorsed by Dr. E. Warren Lindqvist, professor of psychiatry at Westbrook Institute of Medicine, who said:
          <blockquote>“Modern sleep and dream research teaches us-as does Martin Halvorsen’s book Private Sin or Public Sin-that all human activities, including art and politics, are products of the human brain, and that each of us has the privilege and responsibility of using it and communicating its creations.”</blockquote>
        </li>
      </ul>

      <div class="cta">
        <div class="cta__label">SEE MARTIN’S HOMEPAGE FOR MORE DETAILS:</div>
        <div class="cta__url">www.martin-halvorsen.org</div>
      </div>
    </div>
  </section>
</body>
</html>
```